Copper Ridge Hitters Baseball Club (CRH)

Looking for a new web page for Middle School/High School focused baseball club that works with elite prospects. This site will introduce our program to the Northern Virginia area. We will need the ability to sell merchandise and 4+ Services

We would like to use a color theme that goes with our label attached.

We also already own the CRH-VX.com

Industry/Entity Type

Sports Baseball

Coding

Coded - Design and coding required

Number of Pages Required

5+ page

Colors
0054AA
0677BA
7BADD7
CADEEF
E8F1F8

Requirements
Must have
• Ability to upload photos. Page for player profiles/Program Description/Game stats and standings
Nice to have
• pinelakeprospectsball.com otterballclub.net quarrygritballclub.com

```html
<!DOCTYPE html>
<html lang="en">
<head>
<meta charset="utf-8">
<title>Copper Ridge Hitters Baseball Club</title>
<link rel="stylesheet" href="https://fonts.googleapis.com/css2?family=Bebas+Neue&family=Kumbh+Sans:wght@400;500;600;700&display=swap">
<style>
:root{
  --navy:#0c2449;
  --navy-deep:#081a36;
  --orange:#f26a21;
  --green:#7a9a1e;
  --ink:#1b1b1b;
  --muted:#d7dde8;
  --white:#ffffff;
  --head:"Bebas Neue", sans-serif;
  --body:"Kumbh Sans", sans-serif;
}
*{box-sizing:border-box;margin:0;padding:0}
html,body{width:1200px;height:4043px;overflow:hidden}
body{font-family:var(--body);color:var(--ink);background:var(--white);position:relative}
.abs{position:absolute}
a{color:inherit;text-decoration:none}
.btn{position:absolute;display:flex;align-items:center;justify-content:center;gap:6px;font:700 12px/1 var(--body);letter-spacing:.06em;text-transform:uppercase}
.btn svg{width:10px;height:10px}
.btn-orange{background:var(--orange);color:var(--white)}
.btn-outline-white{border:2px solid var(--white);color:var(--white)}
.btn-outline-navy{border:2px solid var(--navy);color:var(--navy)}
.kicker{position:absolute;font:500 15px/1 var(--body);text-transform:uppercase;letter-spacing:-.01em}
.title{position:absolute;font:400 52px/1 var(--head);letter-spacing:.04em;text-transform:uppercase}
.photo{position:absolute}

/* header */
.site-header{position:absolute;left:0;top:0;width:1200px;height:107px;background:var(--white)}
.brand{position:absolute;left:158px;top:22px;display:flex;align-items:center;gap:10px}
.brand-dot{width:46px;height:46px;border-radius:50%;background:var(--navy)}
.brand-name{font:400 44px/1 var(--head);color:var(--navy);letter-spacing:.04em}
.topbar{position:absolute;left:275px;top:42px;width:765px;height:1px;background:#dcdcdc}
.contact{position:absolute;top:5px;display:flex;align-items:center;gap:12px;font:500 14px/1 var(--body);color:#333}
.contact .ic{width:34px;height:34px;border-radius:50%;background:var(--orange);display:flex;align-items:center;justify-content:center}
.contact .ic svg{width:15px;height:15px}
.nav{position:absolute;left:300px;top:67px;display:flex;gap:0;font:500 14px/1 var(--body);letter-spacing:.05em;color:#222}
.nav span{padding:0 16px;border-left:1px solid #555}
.nav span:first-child{padding-left:0;border:0;color:var(--orange)}
.nav-cta{left:891px;top:55px;width:149px;height:39px;background:var(--navy);color:var(--white)}

/* hero */
.hero{position:absolute;left:0;top:107px;width:1200px;height:510px;background:linear-gradient(90deg,#2a2a2a 0%,#3a3534 35%,#1e1e1e 60%,#141414 100%);overflow:hidden}
.hero-photo{left:80px;top:0;width:520px;height:510px;background:radial-gradient(ellipse at 50% 45%,#7a2a2a 0%,#4a3b36 40%,rgba(40,36,35,0) 75%)}
.hero-mark{position:absolute;right:-10px;top:-30px;font:400 430px/1 var(--head);color:rgba(255,255,255,.05);letter-spacing:.02em}
.hero h1{position:absolute;left:587px;top:128px;font:400 57px/63px var(--head);color:var(--white);letter-spacing:.05em}
.hero .btn{left:587px;top:330px;width:149px;height:40px}
.arrow{position:absolute;width:22px;height:38px}

/* about */
.about-photo{left:158px;top:728px;width:432px;height:332px;border-radius:36px;background:linear-gradient(180deg,#9bb3cc 0%,#c9c3a4 45%,#8d9c6a 100%)}
.about-text{position:absolute;left:609px;top:839px;width:430px;font:400 15px/27px var(--body);color:#2a2a2a}

/* news */
.news{position:absolute;left:0;top:1114px;width:1200px;height:596px;background:var(--navy);overflow:hidden}
.news .mark{position:absolute;right:-30px;top:-20px;font:400 360px/1 var(--head);color:rgba(255,255,255,.04)}
.news-rule{position:absolute;left:470px;top:108px;width:520px;height:1px;background:rgba(255,255,255,.15)}
.news-ball{left:988px;top:83px;width:50px;height:50px;border-radius:50%;background:#f4f1ea}
.card-news{position:absolute;top:166px;width:274px;color:var(--white)}
.card-news .img{position:relative;width:274px;height:169px}
.card-news .date{position:absolute;right:-8px;bottom:0;width:196px;height:28px;background:var(--green);clip-path:polygon(8% 0,100% 0,96% 100%,0 100%);font:500 13px/28px var(--body);text-align:center}
.card-news h3{margin-top:22px;font:400 20px/27px var(--head);letter-spacing:.05em}
.card-news p{margin-top:13px;font:400 14px/25px var(--body);color:var(--muted)}
.card-news .more{display:flex;align-items:center;gap:6px;margin-top:22px;font:700 12px/1 var(--body);color:var(--orange);letter-spacing:.05em}
.card-news .more svg{width:10px;height:10px}

/* services */
.service{position:absolute;width:432px;height:259px;overflow:hidden;color:var(--white)}
.service h3{position:absolute;left:21px;top:134px;width:400px;font:400 20px/28px var(--head);letter-spacing:.06em}
.service .btn{left:21px;top:203px;width:150px;height:34px;font-size:11px}

/* players */
.players{position:absolute;left:0;top:2486px;width:1200px;height:607px;background:radial-gradient(ellipse at 40% 20%,#17396b 0%,var(--navy) 55%,var(--navy-deep) 100%)}
.player{position:absolute;top:166px;width:205px;text-align:center;color:var(--white)}
.player .img{width:205px;height:226px;border-radius:14px 14px 38px 38px}
.player .name{margin-top:14px;font:400 20px/1 var(--head);color:var(--orange);letter-spacing:.06em}
.player .role{margin-top:6px;font:400 14px/1 var(--body)}
.socials{display:flex;justify-content:center;gap:10px;margin-top:12px}
.socials i{display:block;width:27px;height:27px;background:var(--green)}
.player .btn{position:relative;margin:19px auto 0;width:141px;height:34px;font-size:11px}

/* store */
.product{position:absolute;top:3258px;width:206px;height:268px;border:2px solid #c8c8c8;text-align:center}
.product .img{position:absolute;left:30px;top:20px;width:142px;height:120px}
.product h3{position:absolute;left:0;right:0;top:178px;font:400 22px/1 var(--head);color:var(--navy);letter-spacing:.06em}
.product .btn{left:32px;top:207px;width:138px;height:33px;font-size:11px}

/* footer */
.footer{position:absolute;left:0;top:3663px;width:1200px;height:380px;background:var(--navy);color:var(--white)}
.footer-notch{position:absolute;left:0;top:3663px;width:178px;height:18px;background:var(--white);clip-path:polygon(0 0,160px 0,100% 100%,0 100%)}
.footer .brand-dot{background:var(--white)}
.footer .brand-name{color:var(--white)}
.f-col{position:absolute;top:86px}
.f-col h4{font:400 19px/1 var(--head);letter-spacing:.06em}
.f-links{margin-top:12px;list-style:none;font:400 14px/28px var(--body)}
.f-links li::before{content:"›";color:var(--orange);margin-right:8px;font-weight:700}
.f-contact{margin-top:14px;font:400 14px/20px var(--body)}
.f-contact div{display:flex;gap:12px;margin-bottom:18px}
.f-contact svg{width:13px;height:13px;flex:none;margin-top:3px}
.f-sub p{margin-top:12px;font:400 14px/20px var(--body);width:260px}
.f-input{margin-top:20px;width:256px;height:41px;background:var(--white);color:#666;font:400 14px/41px var(--body);padding-left:13px}
.f-sub .btn{position:relative;margin-top:9px;width:256px;height:39px}
.f-social{position:absolute;left:158px;top:232px;display:flex;gap:10px}
.f-social i{display:block;width:34px;height:34px;background:var(--green)}
.f-rule{position:absolute;left:158px;top:321px;width:882px;height:1px;background:rgba(255,255,255,.15)}
.copyright{position:absolute;left:0;right:0;top:342px;text-align:center;font:400 13px/1 var(--body);letter-spacing:.04em;color:var(--muted)}
</style>
</head>
<body>

<svg width="0" height="0" style="position:absolute">
  <defs>
    <symbol id="arr" viewBox="0 0 10 10"><path d="M1 5h7M5 2l3 3-3 3" fill="none" stroke="currentColor" stroke-width="1.8"/></symbol>
    <symbol id="chev-l" viewBox="0 0 22 38"><path d="M20 2 3 19l17 17" fill="none" stroke="currentColor" stroke-width="2.2"/></symbol>
    <symbol id="chev-r" viewBox="0 0 22 38"><path d="M2 2l17 17L2 36" fill="none" stroke="currentColor" stroke-width="2.2"/></symbol>
    <symbol id="mail" viewBox="0 0 16 16"><rect x="1.5" y="3.5" width="13" height="9" rx="1" fill="currentColor"/><path d="M2 4l6 5 6-5" fill="none" stroke="#fff" stroke-width="1.2"/></symbol>
    <symbol id="phone" viewBox="0 0 16 16"><path d="M4 1.5l2.5 3-1.3 1.6c.8 1.8 2 3 3.8 3.8l1.6-1.3 3 2.5-1.6 2.4C7.5 13.5 2.5 8.5 1.6 3.1z" fill="currentColor"/></symbol>
    <symbol id="pin" viewBox="0 0 16 16"><path d="M8 1a5 5 0 0 0-5 5c0 4 5 9 5 9s5-5 5-9a5 5 0 0 0-5-5z" fill="currentColor"/><circle cx="8" cy="6" r="2" fill="#0c2449"/></symbol>
    <symbol id="send" viewBox="0 0 10 10"><path d="M1 5 9 1 6 9 5 6z" fill="currentColor"/></symbol>
  </defs>
</svg>

<!-- header -->
<header class="site-header">
  <div class="brand" style="top:26px"><span class="brand-dot"></span><span class="brand-name">CRH</span></div>
  <div class="topbar"></div>
  <div class="contact" style="left:690px"><span class="ic" style="color:#fff"><svg><use href="#mail"/></svg></span>coach.hale@crh-vx.com</div>
  <div class="contact" style="left:897px"><span class="ic" style="color:#fff"><svg><use href="#phone"/></svg></span>555-014-2290</div>
  <nav class="nav"><span>HOME</span><span>ABOUT US</span><span>SERVICES</span><span>NEWS</span><span>MERCHANDISE</span><span>CONTACT</span></nav>
  <a class="btn nav-cta">Player Profiles</a>
</header>

<!-- hero -->
<section class="hero">
  <div class="hero-mark">CRH</div>
  <div class="photo hero-photo" role="img" aria-label="Young batter in red helmet ready to swing"></div>
  <h1>ATHLETES WILL ALWAYS<br>FIND THEMSELVES IN<br>RIGHT PLACES.</h1>
  <a class="btn btn-orange">Learn More <svg><use href="#arr"/></svg></a>
  <svg class="arrow" style="left:92px;top:236px;color:#fff"><use href="#chev-l"/></svg>
  <svg class="arrow" style="left:1083px;top:236px;color:#fff"><use href="#chev-r"/></svg>
</section>

<!-- about -->
<section>
  <div class="photo about-photo" role="img" aria-label="Young player in helmet sprinting between bases"></div>
  <div class="kicker" style="left:609px;top:710px;color:#333">About Us</div>
  <h2 class="title" style="left:609px;top:734px;color:var(--navy)">Copper Ridge Hitters</h2>
  <h2 class="title" style="left:609px;top:785px;color:var(--orange);font-size:42px">Baseball Club</h2>
  <p class="about-text">Athletes will create exciting scoring opportunities and put pressure on an opposing defense. But the mindset and athletic ability to take advantage of a team’s mistakes is something that can be coached and honed. Injury prevention and skill development are optimally learned through movement pattern training and proper conditioning.</p>
  <a class="btn btn-orange" style="left:609px;top:1020px;width:151px;height:40px">Learn More <svg><use href="#arr"/></svg></a>
</section>

<!-- news -->
<section class="news">
  <div class="mark">CRH</div>
  <div class="kicker" style="left:158px;top:60px;color:#fff">Latest News</div>
  <h2 class="title" style="left:158px;top:84px;color:#fff">Baseball News</h2>
  <div class="news-rule"></div>
  <div class="photo news-ball" role="img" aria-label="Baseball"></div>

  <article class="card-news" style="left:158px">
    <div class="img" style="background:linear-gradient(180deg,#6f8a4a 0%,#a5673f 60%,#c08458 100%)" role="img" aria-label="Pitcher throwing with umpire behind"><span class="date">19TH NOVEMBER, 2021</span></div>
    <h3>Sed do eiusmod tempor incididunt<br>ut labore et dolore magna</h3>
    <p>Quis nostrud exercitation ullamco laboris nisi ut aliquip ex ea commodo conseq..</p>
    <a class="more">Learn More <svg><use href="#arr"/></svg></a>
  </article>
  <article class="card-news" style="left:458px">
    <div class="img" style="background:linear-gradient(180deg,#6b6f5a 0%,#8e7a5e 55%,#b48a5f 100%)" role="img" aria-label="Batter at home plate with catcher"><span class="date">19TH NOVEMBER, 2021</span></div>
    <h3>Sed do eiusmod tempor incididunt<br>ut labore et dolore magna</h3>
    <p>Quis nostrud exercitation ullamco laboris nisi ut aliquip ex ea commodo conseq..</p>
    <a class="more">Learn More <svg><use href="#arr"/></svg></a>
  </article>
  <article class="card-news" style="left:759px">
    <div class="img" style="background:linear-gradient(135deg,#c9b28a 0%,#9b7a52 50%,#b35a2f 100%)" role="img" aria-label="Bats, gloves and baseballs laid out"><span class="date">19TH NOVEMBER, 2021</span></div>
    <h3>Sed do eiusmod tempor incididunt<br>ut labore et dolore magna</h3>
    <p>Quis nostrud exercitation ullamco laboris nisi ut aliquip ex ea commodo conseq..</p>
    <a class="more">Learn More <svg><use href="#arr"/></svg></a>
  </article>
  <svg class="arrow" style="left:120px;top:232px;color:#fff;width:16px;height:28px"><use href="#chev-l"/></svg>
  <svg class="arrow" style="left:1062px;top:232px;color:#fff;width:16px;height:28px"><use href="#chev-r"/></svg>
</section>

<!-- services -->
<section>
  <div class="kicker" style="left:158px;top:1769px;color:#333">Services</div>
  <h2 class="title" style="left:158px;top:1793px;color:var(--navy)">What We Do</h2>
  <a class="btn btn-orange" style="left:849px;top:1771px;width:191px;height:39px">View All Services <svg><use href="#arr"/></svg></a>

  <div class="service" style="left:158px;top:1885px">
    <div class="photo" style="inset:0;background:linear-gradient(180deg,#5a5a5a 0%,#2e2e2e 100%)" role="img" aria-label="Baseball resting on grass in black and white"></div>
    <h3>Sed do eiusmod tempor incididunt ut labore et dolore magna exercitation ullamco</h3>
    <a class="btn btn-outline-white">Learn More <svg><use href="#arr"/></svg></a>
  </div>
  <div class="service" style="left:609px;top:1885px">
    <div class="photo" style="inset:0;background:linear-gradient(180deg,#e0672b 0%,#d2592a 100%)" role="img" aria-label="Ball on orange infield dirt"></div>
    <h3>Sed do eiusmod tempor incididunt ut labore et dolore magna exercitation ullamco</h3>
    <a class="btn btn-outline-white">Learn More <svg><use href="#arr"/></svg></a>
  </div>
  <div class="service" style="left:158px;top:2165px">
    <div class="photo" style="inset:0;background:linear-gradient(180deg,#7a8a6a 0%,#5c6d4d 60%,#4a4a3c 100%)" role="img" aria-label="Player in blue jersey on the field"></div>
    <h3>Sed do eiusmod tempor incididunt ut labore et dolore magna exercitation ullamco</h3>
    <a class="btn btn-outline-white">Learn More <svg><use href="#arr"/></svg></a>
  </div>
  <div class="service" style="left:609px;top:2165px">
    <div class="photo" style="inset:0;background:linear-gradient(135deg,#2c3a2e 0%,#3b2a24 55%,#7a3a24 100%)" role="img" aria-label="Batter gripping bat in helmet"></div>
    <h3>Sed do eiusmod tempor incididunt ut labore et dolore magna exercitation ullamco</h3>
    <a class="btn btn-outline-white">Learn More <svg><use href="#arr"/></svg></a>
  </div>
</section>

<!-- players -->
<section class="players">
  <div class="kicker" style="left:158px;top:62px;color:#fff">Sports Team</div>
  <h2 class="title" style="left:158px;top:86px;color:#fff">Our Player</h2>
  <a class="btn btn-outline-white" style="left:849px;top:63px;width:191px;height:38px;border-color:var(--orange)">View All Profiles <svg><use href="#arr"/></svg></a>

  <div class="player" style="left:158px">
    <div class="img" style="background:linear-gradient(180deg,#e4ecf3 0%,#9db7d6 60%,#2f62b3 100%)" role="img" aria-label="Junior player portrait in blue helmet"></div>
    <div class="name">Evan Brooks</div><div class="role">Junior Player</div>
    <div class="socials"><i></i><i></i><i></i></div>
    <a class="btn btn-outline-white">View Profile <svg><use href="#arr"/></svg></a>
  </div>
  <div class="player" style="left:384px">
    <div class="img" style="background:linear-gradient(180deg,#eef0f2 0%,#cfd5de 60%,#aab3c0 100%)" role="img" aria-label="Junior player portrait in pinstripe uniform"></div>
    <div class="name">Evan Brooks</div><div class="role">Junior Player</div>
    <div class="socials"><i></i><i></i><i></i></div>
    <a class="btn btn-outline-white">View Profile <svg><use href="#arr"/></svg></a>
  </div>
  <div class="player" style="left:609px">
    <div class="img" style="background:linear-gradient(180deg,#f0f0f0 0%,#c9c9c9 55%,#3a3a3a 100%)" role="img" aria-label="Junior player portrait in red helmet"></div>
    <div class="name">Evan Brooks</div><div class="role">Junior Player</div>
    <div class="socials"><i></i><i></i><i></i></div>
    <a class="btn btn-outline-white">View Profile <svg><use href="#arr"/></svg></a>
  </div>
  <div class="player" style="left:835px">
    <div class="img" style="background:linear-gradient(180deg,#f3f3f3 0%,#d8d8d8 50%,#d94a3a 100%)" role="img" aria-label="Junior player portrait in red shirt"></div>
    <div class="name">Evan Brooks</div><div class="role">Junior Player</div>
    <div class="socials"><i></i><i></i><i></i></div>
    <a class="btn btn-outline-white">View Profile <svg><use href="#arr"/></svg></a>
  </div>
  <svg class="arrow" style="left:120px;top:278px;color:#fff;width:16px;height:28px"><use href="#chev-l"/></svg>
  <svg class="arrow" style="left:1062px;top:278px;color:#fff;width:16px;height:28px"><use href="#chev-r"/></svg>
</section>

<!-- store -->
<section>
  <div class="kicker" style="left:0;right:0;top:3154px;text-align:center;color:#333">Merchandise</div>
  <h2 class="title" style="left:0;right:0;top:3178px;text-align:center;color:var(--navy)">Visit Our Store</h2>

  <div class="product" style="left:158px">
    <div class="photo img" style="background:radial-gradient(circle,#b0703a 0%,#e9d6c4 70%,#fff 100%)" role="img" aria-label="Glove with ball and bat"></div>
    <h3>Baseball Combo</h3>
    <a class="btn btn-orange">Go To Store <svg><use href="#arr"/></svg></a>
  </div>
  <div class="product" style="left:384px">
    <div class="photo img" style="background:radial-gradient(circle,#e9a866 0%,#f6e3cc 60%,#fff 100%)" role="img" aria-label="Two crossed wooden bats"></div>
    <h3>Baseball Bat</h3>
    <a class="btn btn-orange">Go To Store <svg><use href="#arr"/></svg></a>
  </div>
  <div class="product" style="left:609px">
    <div class="photo img" style="background:radial-gradient(circle,#2a2a2a 0%,#9a9a9a 60%,#fff 100%)" role="img" aria-label="Black batting helmet with face guard"></div>
    <h3>Baseball Helmet</h3>
    <a class="btn btn-orange">Go To Store <svg><use href="#arr"/></svg></a>
  </div>
  <div class="product" style="left:835px">
    <div class="photo img" style="background:radial-gradient(circle,#e6e51c 0%,#f3f18f 55%,#fff 100%)" role="img" aria-label="Yellow and black sports jersey"></div>
    <h3>Sports Jersey</h3>
    <a class="btn btn-orange">Go To Store <svg><use href="#arr"/></svg></a>
  </div>

  <a class="btn btn-outline-navy" style="left:511px;top:3561px;width:176px;height:39px">Visit Our Store <svg><use href="#arr"/></svg></a>
</section>

<!-- footer -->
<footer class="footer">
  <div class="brand" style="left:158px;top:86px"><span class="brand-dot"></span><span class="brand-name">CRH</span></div>
  <div class="f-social"><i></i><i></i><i></i></div>

  <div class="f-col" style="left:397px">
    <h4>Quick Links</h4>
    <ul class="f-links"><li>Home</li><li>About Us</li><li>Services</li><li>News</li><li>Merchandise</li><li>Contact Us</li></ul>
  </div>
  <div class="f-col" style="left:552px">
    <h4>Contact Us</h4>
    <div class="f-contact">
      <div><svg style="color:var(--orange)"><use href="#pin"/></svg><span>beatae vitae dicta sunt<br>enim ipsam voluptatem</span></div>
      <div><svg style="color:var(--orange)"><use href="#phone"/></svg><span>Phone:<br>555-014-2290</span></div>
      <div><svg style="color:var(--orange)"><use href="#mail"/></svg><span>Email:<br>coach.hale@crh-vx.com</span></div>
    </div>
  </div>
  <div class="f-col f-sub" style="left:784px">
    <h4>Subscribe Newsletter</h4>
    <p>Subscribe our newsletter to get latest updates direct your inbox.</p>
    <div class="f-input">Enter your email</div>
    <a class="btn btn-orange">Subscribe Now <svg><use href="#send"/></svg></a>
  </div>

  <div class="f-rule"></div>
  <div class="copyright">COPYRIGHT © 2021 COPPER RIDGE HITTERS BASEBALL CLUB. ALL RIGHTS RESERVED.</div>
</footer>
<div class="footer-notch"></div>

</body>
</html>
```